Wholesale in Gold Jewellery & Gold Bullion

We are an established gold jewellery and gold bullion wholesaler selling these products to international clients. We already have a name and logo of our company, hence please view attached current card design. We need a completely new design to compliment our business and industry and the final design should be new and elegant.

Contact Information for Business Card

New card details must be same as per current card. Like logo, name, tel no. & etc.

Colors

Designer to choose colors to be used in the design.

```html
<!DOCTYPE html>
<html lang="en">
<head>
<meta charset="utf-8">
<title>Aurelian &amp; Co — Business Card</title>
<link href="https://fonts.googleapis.com/css2?family=Cinzel:wght@400;500&family=Open+Sans:wght@400&display=swap" rel="stylesheet">
<style>
  :root {
    --card-black: #161616;
    --card-edge: #0c0c0c;
    --page: #e9e7e3;
    --gold: #c9a64a;
    --gold-light: #e3c677;
    --ink-light: #d9d9d9;
  }
  html, body {
    margin: 0;
    padding: 0;
    width: 1200px;
    height: 727px;
    overflow: hidden;
    background: var(--page);
  }
  .card {
    position: relative;
    width: 1200px;
    height: 727px;
    background: radial-gradient(ellipse at 60% 30%, #1d1d1d 0%, var(--card-black) 60%, var(--card-edge) 100%);
    color: var(--ink-light);
    font-family: "Open Sans", Arial, sans-serif;
  }
  .brand {
    position: absolute;
    right: 150px;
    top: 120px;
    display: flex;
    flex-direction: column;
    align-items: center;
    color: var(--gold);
    font-family: "Cinzel", "Times New Roman", serif;
    font-weight: 400;
  }
  .brand-dot {
    width: 96px;
    height: 96px;
    border-radius: 50%;
    background: var(--gold);
    margin-bottom: 22px;
  }
  .brand-name {
    font-size: 44px;
    letter-spacing: 2px;
    line-height: 1;
  }
  .brand-suffix {
    font-size: 16px;
    letter-spacing: 3px;
    margin-top: 6px;
  }
  .rule {
    position: absolute;
    left: 300px;
    right: 110px;
    top: 392px;
    height: 1.5px;
    background: var(--gold);
  }
  .person {
    position: absolute;
    left: 110px;
    top: 330px;
    color: var(--gold);
    font-family: "Cinzel", "Times New Roman", serif;
  }
  .person-name {
    font-size: 40px;
    letter-spacing: 2px;
    line-height: 1;
    font-weight: 500;
  }
  .person-title {
    font-size: 21px;
    margin-top: 6px;
    font-family: "Cinzel", "Times New Roman", serif;
    text-transform: none;
  }
  .phones {
    position: absolute;
    left: 130px;
    top: 470px;
    list-style: none;
    margin: 0;
    padding: 0;
    font-size: 24px;
  }
  .phones li {
    display: flex;
    align-items: center;
    height: 44px;
  }
  .phones svg {
    width: 26px;
    height: 24px;
    margin-right: 22px;
    fill: var(--gold);
  }
  .address {
    position: absolute;
    right: 110px;
    top: 440px;
    text-align: right;
    font-size: 24px;
    line-height: 40px;
  }
  .address-line {
    display: flex;
    justify-content: flex-end;
    align-items: center;
  }
  .address-line svg {
    width: 24px;
    height: 24px;
    margin-left: 18px;
    fill: var(--gold);
  }
  .address-line .spacer {
    display: inline-block;
    width: 24px;
    margin-left: 18px;
  }
</style>
</head>
<body>
  <main class="card">
    <header class="brand">
      <span class="brand-dot" aria-hidden="true"></span>
      <span class="brand-name">AURELIAN &amp; CO</span>
      <span class="brand-suffix">PTE LTD</span>
    </header>

    <div class="rule" aria-hidden="true"></div>

    <section class="person">
      <div class="person-name">ROHAN VELLAKAR</div>
      <div class="person-title">Director</div>
    </section>

    <ul class="phones">
      <li>
        <svg viewBox="0 0 26 24" aria-label="Telephone"><path d="M2 8c0-3 4-5 11-5s11 2 11 5v2h-6V8c-1-1-9-1-10 0v2H2z"/><rect x="5" y="12" width="16" height="10" rx="2"/></svg>
        +65 6100 2400
      </li>
      <li>
        <svg viewBox="0 0 26 24" aria-label="Mobile"><path d="M8 1h10a2 2 0 0 1 2 2v18a2 2 0 0 1-2 2H8a2 2 0 0 1-2-2V3a2 2 0 0 1 2-2zm0 3v14h10V4z"/></svg>
        +65 9100 3456
      </li>
      <li>
        <svg viewBox="0 0 26 24" aria-label="Fax"><rect x="7" y="2" width="12" height="7"/><rect x="2" y="9" width="22" height="12" rx="2"/><rect x="8" y="15" width="10" height="8" fill="#161616"/></svg>
        +65 6100 2471
      </li>
    </ul>

    <address class="address" style="font-style:normal">
      <div class="address-line">12 Linden Quay,
        <svg viewBox="0 0 24 24" aria-label="Location"><path d="M12 1a8 8 0 0 1 8 8c0 6-8 14-8 14S4 15 4 9a8 8 0 0 1 8-8zm0 5a3 3 0 1 0 0 6 3 3 0 0 0 0-6z"/></svg>
      </div>
      <div class="address-line">Singapore 100021<span class="spacer"></span></div>
      <div class="address-line">rohan@aurelianco.com
        <svg viewBox="0 0 24 24" aria-label="Email"><path d="M2 5h20v14H2zm2 2v1l8 5 8-5V7l-8 5z"/></svg>
      </div>
    </address>
  </main>
</body>
</html>
```